Outdoor Billboard on PVC (double sides)

Hello, i need special design for billboard which is located 15 meters away from the main road. Measures form Billboard: 8 meters X 2 meters. I need Billboard for Window tinting. I have one picture (white Brevanti) which you can use as a main BIG Picture- or you have better idea i am so open to your suggestions. Billboard has to be shocking ... i want to make it look like this is similiar way from style. I have a lot of pictures from my cars which i have done in my garage which we can use it. I dont know if you can use this ... quality? On the billboard so it blames be turn left in 30Meter. My logo wants bi attached- please use it on black background. text which schould be down on the Billboard: Proffesionale Tint my logo VELUNAR put somewhere where looks cool Phone: 0681 2495 307 E-mail: marlow.velunar@kestramail.com Website: www. velunar-glasdunkel.at

Target Market(s)

This billboard wants to be on the border between two countrys..i have my garage company here on the border- where ia am making window. A lot of cars are driving each day nearby so I want that people see this and so they look at where they have left to my garage.

Colors

Designer to choose colors to be used in the design.

Requirements
Must have
• Billboard schould have a BiG picture from white Brevanti with my logo on the side and text Proffesional scarf tint. Down on the board it schould be info Tel, email, website. This measures 8x2 meters

```html
<!DOCTYPE html>
<html lang="de">
<head>
<meta charset="utf-8">
<title>VELUNAR – Professionelle Scheibentönung</title>
<link rel="stylesheet" href="https://fonts.googleapis.com/css2?family=Oswald:wght@600;700&family=Open+Sans:wght@600&display=swap">
<style>
  :root {
    --stage: #e9ecef;
    --paper: #ffffff;
    --ink: #111111;
    --night: #000000;
    --signal: #e31b23;
    --car-light: #eceef0;
    --car-mid: #b9bdc2;
    --car-dark: #5d6166;
  }
  * { margin: 0; padding: 0; box-sizing: border-box; }
  html, body {
    width: 1200px;
    height: 962px;
    overflow: hidden;
    background: var(--stage);
  }
  .canvas {
    position: relative;
    width: 1200px;
    height: 962px;
  }
  .billboard {
    position: absolute;
    left: 20px;
    top: 333px;
    width: 1285px;
    height: 328px;
    transform: scale(0.9027);
    transform-origin: 0 0;
    background: var(--paper);
    overflow: hidden;
    box-shadow: 0 6px 24px rgba(0,0,0,0.18);
  }
  .billboard__shapes {
    position: absolute;
    inset: 0;
  }
  .car-photo {
    position: absolute;
    left: 492px;
    top: 58px;
    width: 768px;
    height: 248px;
    border-radius: 120px 150px 40px 60px / 110px 120px 40px 50px;
    background: linear-gradient(180deg, var(--car-light) 0%, var(--car-mid) 62%, var(--car-dark) 100%);
  }
  .headline {
    position: absolute;
    left: 22px;
    top: 26px;
    font-family: "Oswald", "Arial Narrow", sans-serif;
    font-weight: 700;
    line-height: 1;
    letter-spacing: -0.5px;
    transform: scaleX(0.86);
    transform-origin: 0 0;
  }
  .headline__top {
    display: block;
    color: var(--signal);
    font-size: 76px;
  }
  .headline__bottom {
    display: block;
    color: var(--ink);
    font-size: 79px;
    margin-top: 2px;
  }
  .contact {
    position: absolute;
    left: 22px;
    top: 224px;
    list-style: none;
    font-family: "Open Sans", Arial, sans-serif;
    font-weight: 600;
    font-size: 20.5px;
    color: var(--ink);
  }
  .contact__item {
    display: flex;
    align-items: center;
    height: 32px;
  }
  .contact__icon {
    width: 15px;
    height: 15px;
    margin-right: 10px;
    flex: none;
  }
  .brand {
    position: absolute;
    right: 34px;
    top: 20px;
    display: flex;
    flex-direction: column;
    align-items: center;
  }
  .brand__dot {
    width: 40px;
    height: 40px;
    border-radius: 50%;
    background: var(--signal);
    margin-bottom: 6px;
  }
  .brand__name {
    font-family: "Oswald", "Arial Narrow", sans-serif;
    font-weight: 700;
    font-size: 22px;
    letter-spacing: 1px;
    color: var(--signal);
    line-height: 1;
  }
</style>
</head>
<body>
<main class="canvas">
  <section class="billboard">
    <svg class="billboard__shapes" viewBox="0 0 1285 328" width="1285" height="328" aria-hidden="true">
      <polygon fill="var(--signal)" points="630,0 1285,0 1285,328 630,328 520,180"/>
      <polygon fill="var(--night)" points="702,0 1285,0 1285,328 705,328 590,180"/>
    </svg>

    <div class="car-photo" role="img" aria-label="White Brevanti sports car, side view"></div>

    <h1 class="headline">
      <span class="headline__top">PROFFESIONELLE</span>
      <span class="headline__bottom">SCHEIBENTÖNUNG</span>
    </h1>

    <ul class="contact">
      <li class="contact__item">
        <svg class="contact__icon" viewBox="0 0 15 15" aria-hidden="true">
          <rect width="15" height="15" fill="var(--signal)"/>
          <path d="M4 3.5 L6 3.5 L6.8 5.6 L5.8 6.6 Q7 8.6 8.6 9.4 L9.6 8.4 L11.5 9.2 L11.5 11.2 Q7 11.5 3.8 7.4 Q3.3 5.5 4 3.5 Z" fill="#fff"/>
        </svg>
        0681 2495 307
      </li>
      <li class="contact__item">
        <svg class="contact__icon" viewBox="0 0 15 15" aria-hidden="true">
          <rect width="15" height="15" fill="var(--signal)"/>
          <rect x="3" y="4.5" width="9" height="6" fill="#fff"/>
          <path d="M3 4.5 L7.5 8 L12 4.5" fill="none" stroke="var(--signal)" stroke-width="1"/>
        </svg>
        marlow.velunar@kestramail.com
      </li>
      <li class="contact__item">
        <svg class="contact__icon" viewBox="0 0 15 15" aria-hidden="true">
          <rect width="15" height="15" fill="var(--signal)"/>
          <circle cx="7.5" cy="7.5" r="4" fill="none" stroke="#fff" stroke-width="1"/>
          <path d="M3.5 7.5 H11.5 M7.5 3.5 V11.5" stroke="#fff" stroke-width="0.8"/>
        </svg>
        www.velunar-glasdunkel.at
      </li>
    </ul>

    <div class="brand">
      <span class="brand__dot"></span>
      <span class="brand__name">VELUNAR</span>
    </div>
  </section>
</main>
</body>
</html>
```